Torvanex needs a Monthly Newsletter

We need a newsletter design for a company located in Sydney Australia. We are an IT Services and Software Development company with both arms separated as a business. We would like to see designs that follow the same elements that our website has being www.torvanex.com.au.
It needs an element of our corporate blue logo in it and would like the same colour elements included throughout the file.
The file needs to be MailChimp compatible and we would need all the files being HTML, the graphics, the PSD files, the MailChimp ready file, etc.

```html
<!DOCTYPE html>
<html lang="en">
<head>
<meta charset="utf-8">
<title>Torvanex Monthly Newsletter – May</title>
<link rel="stylesheet" href="https://fonts.googleapis.com/css2?family=Ubuntu:wght@400;500;700&family=Open+Sans:wght@400;700;800&display=swap">
<style>
:root{
  --page-bg:#f0f1f3;
  --card-bg:#ffffff;
  --card-border:#d9dadc;
  --rule:#dedede;
  --brand-blue:#3b86e0;
  --text-dark:#2b2b2b;
  --text-body:#333333;
  --text-muted:#8c8c8c;
  --cta-red:#d9302c;
  --tip-yellow:#fbbd14;
  --fact-green:#5cbd1f;
  --social-blue:#1da1f2;
  --white:#ffffff;
}
*{box-sizing:border-box;margin:0;padding:0}
html,body{width:1200px;height:2874px;overflow:hidden}
body{background:var(--page-bg);font-family:"Ubuntu",sans-serif;color:var(--text-body);position:relative}
.view-online{position:absolute;top:10px;left:0;width:1200px;text-align:center;font-family:"Open Sans",sans-serif;font-size:19px;color:var(--text-muted)}
.view-online u{color:var(--text-muted)}
.card{position:absolute;left:41px;top:43px;width:1116px;height:2783px;background:var(--card-bg);border:2px solid var(--card-border);border-radius:8px;box-shadow:0 2px 6px rgba(0,0,0,.08)}
.block{position:absolute;left:98px;width:1001px}
.rule{position:absolute;left:98px;width:1001px;height:2px;background:var(--rule)}
.brand{top:100px;height:124px;display:flex;align-items:center;justify-content:center;gap:26px}
.brand-dot{width:110px;height:110px;border-radius:50%;background:var(--brand-blue)}
.brand-name{font-size:82px;font-weight:500;letter-spacing:6px;color:var(--brand-blue)}
.issue{top:300px;text-align:center;font-size:25px;color:var(--text-dark)}
.banner{top:398px;height:155px;background:var(--brand-blue);display:flex;align-items:center;justify-content:space-between;padding:0 27px 0 33px}
.banner p{flex:1;text-align:center;color:var(--white);font-size:31px;line-height:42px;padding:0 20px}
.banner svg{width:82px;height:82px;flex:none}
.photo{position:absolute}
.hero{left:98px;top:611px;width:1001px;height:414px;background:linear-gradient(120deg,#dfe6ee 0%,#9eb6cc 35%,#e9eef3 60%,#c4d2df 100%);box-shadow:0 8px 14px rgba(0,0,0,.25)}
.section-head{display:flex;align-items:center;gap:22px}
.section-icon{width:82px;height:82px;flex:none}
.section-title{font-size:40px;line-height:44px;font-weight:400;color:var(--text-dark)}
.website{top:1093px;width:580px}
.website p{margin-top:16px;font-size:25px;line-height:34px}
.btn{position:absolute;background:var(--cta-red);color:var(--white);font-family:"Open Sans",sans-serif;font-weight:800;font-size:28px;letter-spacing:1px;display:flex;align-items:center;justify-content:center;gap:12px;border-radius:4px;box-shadow:0 3px 4px rgba(0,0,0,.25)}
.btn svg{width:12px;height:18px}
.btn-website{left:98px;top:1346px;width:261px;height:79px}
.photo-network{left:697px;top:1099px;width:402px;height:326px;background:linear-gradient(160deg,#1d2a3a 0%,#3b5873 50%,#14202e 100%)}
.promo{position:absolute;top:1487px;height:335px;padding:17px}
.promo-inner{height:100%;border:4px dashed rgba(255,255,255,.9);text-align:center;color:var(--white);font-family:"Open Sans",sans-serif;padding:28px 22px 0}
.promo h2{font-size:31px;font-weight:800;letter-spacing:1px}
.promo p{font-size:22px;line-height:26px}
.tip{left:98px;width:570px;background:var(--tip-yellow)}
.tip .devices{display:flex;justify-content:center;gap:38px;margin:16px 0 14px}
.tip .devices svg{height:56px}
.tip a{color:var(--text-dark);text-decoration:underline}
.fact{left:697px;width:402px;background:var(--fact-green)}
.fact .bulb{margin:10px auto 14px;display:block;width:70px;height:62px}
.case{top:1877px}
.case .section-head{justify-content:flex-start}
.social-dot{position:absolute;right:-13px;top:4px;width:74px;height:74px;border-radius:50%;background:var(--social-blue)}
.case p{font-size:25px;line-height:34px;color:var(--text-body)}
.case .lead{margin-top:40px}
.case .more{margin-top:30px;width:700px}
.btn-case{left:841px;top:2148px;width:259px;height:74px}
.blogs{top:2306px;width:560px}
.blogs ul{list-style:none;margin-top:24px}
.blogs li{font-size:26px;line-height:34px;margin-bottom:12px}
.blogs a{color:var(--text-body);text-decoration:underline}
.photo-desk{left:699px;top:2314px;width:393px;height:244px;background:linear-gradient(135deg,#f4f6f7 0%,#e3e8ea 55%,#f1d86a 100%)}
.footer{top:2642px;height:127px;background:var(--brand-blue);color:var(--white);text-align:center;font-size:26px;line-height:36px;padding-top:27px}
.footer u{color:var(--white)}
</style>
</head>
<body>
<p class="view-online">If you're having trouble viewing this email, you can view it in your <u>browser here</u></p>

<div class="card"></div>

<header class="block brand">
  <span class="brand-dot"></span>
  <span class="brand-name">TORVANEX</span>
</header>
<div class="rule" style="top:275px"></div>
<p class="block issue">Monthly Newsletter – MAY</p>
<div class="rule" style="top:366px"></div>

<section class="block banner">
  <svg viewBox="0 0 82 82" aria-hidden="true"><circle cx="41" cy="41" r="39" fill="#fff"/><rect x="21" y="24" width="40" height="27" rx="2" fill="none" stroke="#3b86e0" stroke-width="4"/><path d="M35 51v7h12v-7M30 59h22" stroke="#3b86e0" stroke-width="4" fill="none"/><path d="M30 40l6 5 12-10" stroke="#3b86e0" stroke-width="3" fill="none"/></svg>
  <p>Torvanex provides highly effective IT solutions and services, with an agile and nimble approach</p>
  <svg viewBox="0 0 82 82" aria-hidden="true"><circle cx="41" cy="41" r="39" fill="#fff"/><circle cx="38" cy="30" r="10" fill="#3b86e0"/><path d="M18 60c0-12 9-18 20-18s16 5 18 10" fill="#3b86e0"/><circle cx="56" cy="56" r="9" fill="#3b86e0"/><path d="M51 56l4 4 6-7" stroke="#fff" stroke-width="2.5" fill="none"/></svg>
</section>
<div class="rule" style="top:582px"></div>

<div class="photo hero" role="img" aria-label="Hands at a keyboard and mouse with a translucent data overlay"></div>
<div class="rule" style="top:1063px"></div>

<section class="block website">
  <div class="section-head">
    <svg class="section-icon" viewBox="0 0 82 82" aria-hidden="true"><circle cx="41" cy="41" r="41" fill="#3b86e0"/><rect x="22" y="24" width="38" height="26" rx="2" fill="none" stroke="#fff" stroke-width="4"/><path d="M36 50v7h10v-7M30 58h22" stroke="#fff" stroke-width="4" fill="none"/></svg>
    <h2 class="section-title">New Website –<br>Give us your feedback!</h2>
  </div>
  <p>We have had our website up for a short while now. Please have a look and give us some feedback! Click here to email us some feedback!</p>
</section>
<a class="btn btn-website">SEE WEBSITE <svg viewBox="0 0 12 18"><path d="M0 0l12 9-12 9z" fill="#fff"/></svg></a>
<div class="photo photo-network" role="img" aria-label="Person in front of a glowing network of connected people at night"></div>
<div class="rule" style="top:1459px"></div>

<section class="promo tip">
  <div class="promo-inner">
    <h2>TIP OF THE MONTH</h2>
    <div class="devices" aria-hidden="true">
      <svg viewBox="0 0 56 56"><rect x="3" y="6" width="50" height="34" rx="2" fill="none" stroke="#2b2b2b" stroke-width="3"/><path d="M22 40v8h12v-8M16 50h24" stroke="#2b2b2b" stroke-width="3" fill="none"/></svg>
      <svg viewBox="0 0 56 56"><rect x="9" y="12" width="38" height="26" rx="2" fill="none" stroke="#2b2b2b" stroke-width="3"/><path d="M3 44h50" stroke="#2b2b2b" stroke-width="3"/></svg>
      <svg viewBox="0 0 44 56"><rect x="4" y="3" width="36" height="50" rx="3" fill="none" stroke="#2b2b2b" stroke-width="3"/><circle cx="22" cy="46" r="2" fill="#2b2b2b"/></svg>
      <svg viewBox="0 0 30 56"><rect x="3" y="3" width="24" height="50" rx="3" fill="none" stroke="#2b2b2b" stroke-width="3"/><circle cx="15" cy="46" r="2" fill="#2b2b2b"/></svg>
    </div>
    <p>Quenlark has stopped producing their most popular Brixel Server... Why? Quenlark Works! Find out how IT is progressing by joining the <a>Quenlark Works Linkvale group</a> ▸ ▸ ▸</p>
  </div>
</section>

<section class="promo fact">
  <div class="promo-inner">
    <h2>DID YOU KNOW?</h2>
    <svg class="bulb" viewBox="0 0 70 62" aria-hidden="true"><path d="M35 8a14 14 0 0 0-8 25v8h16v-8A14 14 0 0 0 35 8z" fill="none" stroke="#fff" stroke-width="3"/><path d="M29 46h12M30 51h10" stroke="#fff" stroke-width="3"/><text x="4" y="34" font-family="Open Sans,sans-serif" font-size="22" font-weight="700" fill="#fff">?</text><text x="54" y="34" font-family="Open Sans,sans-serif" font-size="22" font-weight="700" fill="#fff">?</text></svg>
    <p>Did you know that Vellumbox 2013 integrates with Linkvale? Imagine how powerful that could be for your business!</p>
  </div>
</section>
<div class="rule" style="top:1851px"></div>

<section class="block case">
  <div class="section-head">
    <svg class="section-icon" viewBox="0 0 82 82" aria-hidden="true"><circle cx="41" cy="41" r="41" fill="#3b86e0"/><circle cx="38" cy="30" r="10" fill="none" stroke="#fff" stroke-width="3.5"/><path d="M20 60c0-11 8-17 18-17s18 6 18 17z" fill="none" stroke="#fff" stroke-width="3.5"/><circle cx="55" cy="52" r="7" fill="#3b86e0" stroke="#fff" stroke-width="3"/></svg>
    <h2 class="section-title">Case Study of the Month</h2>
  </div>
  <span class="social-dot"></span>
  <p class="lead">Torvanex has implemented an infrastructure upgrade for Halden Stone &amp; Tile. The upgrade was carried out after consultation to enhance speeds and resolve the overlapping of two servers; one of which belongs to another company of Halden Stone &amp; Tile.</p>
  <p class="more">The upgrade consisted of Internet, Server and virtualisation improvements. To read the full case study:</p>
</section>
<a class="btn btn-case">CLICK HERE <svg viewBox="0 0 12 18"><path d="M0 0l12 9-12 9z" fill="#fff"/></svg></a>
<div class="rule" style="top:2270px"></div>

<section class="block blogs">
  <div class="section-head">
    <svg class="section-icon" viewBox="0 0 82 82" aria-hidden="true"><circle cx="41" cy="41" r="41" fill="#3b86e0"/><path d="M26 18h22l9 9v37H26z" fill="none" stroke="#fff" stroke-width="3.5"/><path d="M32 34h18M32 41h18M32 48h18M32 55h18" stroke="#fff" stroke-width="3"/></svg>
    <h2 class="section-title">Recent Blogs</h2>
  </div>
  <ul>
    <li><a>Three ways to defeat ransom based viruses</a></li>
    <li><a>What should go on your Stackroom?</a></li>
    <li><a>How to achieve productivity for your mobile health workers</a></li>
  </ul>
</section>
<div class="photo photo-desk" role="img" aria-label="Support agent with a headset working at a laptop in a bright office"></div>
<div class="rule" style="top:2599px"></div>

<footer class="block footer">
  You are receiving this email because you subscribed to our newsletter.<br>
  <u>Unsubscribe</u> or change your preferences here.
</footer>
</body>
</html>
```